Travel Company Itinerary and Travel Packet

I run a travel company (agency) that organizes trips (any length i.e. day, week, month, or longer) to countries (Israel, Italy, Greece, etc). Regardless of the destination, we want to provide appealing, professional, and clean materials. We are a firm believer that our product is not just the trip but in everything we do...from our communication to our written/printed materials and online presence. Today we are specifically looking for a template that we can use to share one's trip/itinerary. Ideally what you would create would be a template we could populate with specific information for the client about the day-to-day of their trip, who we are, the hotels they are staying in, the highlights, what to pack, and where to eat, etc. To be more specific, this template should consist of the following:
1. Title Page (including contact info...however this could go where you see fit)
2. About Us (blurb about us at the company),
3. A highlights page of the trip and services included - this could be used as standalone marketing material for our clients to promote trips. (look at the Italy example)
4. A timeline of the process
5. A summary of the trip, bullet point/all one 1 page
6. A day-by-day itinerary page of what they are doing, and where they are staying (each day on its own page - should be the same template repeated for each day.
7. Recommended Hotels to choose from
8. Recommended Restaurants to eat at
9. A pricing page (per person, per group, itemized down to each experience.
10. A packing List
11. A letterhead that could be used for a cover letter
12. Each page should use pictures...a template where one could insert photos per page based on where the trip is going as well as stock imaging that brings the document to life for the reader. (see examples in uploaded files).

We've attached a few that we've seen in the industry that appeals to us and our tastes, but the template we are looking for is even more eye-popping, user-friendly, and communicates a high level of service just by seeing the document. It communicates our brand. Each attached example has elements we like and don't like and will give you. a good picture (we hope), but you'll notice the list we gave you provides a more robust end product...in other words we want more than these examples as we see great potential in including each layer of information with the ability to pick and choose what to include (from all of it to just the highlights page).

Link to Brand Assets- https://files.morvenbay.net/shared/8Kq2Tz7Lw4Xp1Rn6Vb3Yc9Hd5Fj0Ms?view=open
Updates

We need a few days to review the designs and had a few requests for an extension if possible. I've also uploaded sample itineraries for Israel as requested by a few designers. Much appreciated

Target Market(s)

Any client of ours traveling - school, groups, families, big spenders etc

Industry/Entity Type

Travel Industry

Requirements
Must have
• See above list - if clarification is needed, I'm happy to give.

```html
<!DOCTYPE html>
<html lang="en">
<head>
<meta charset="utf-8">
<title>Wayfarlo Travel Packet Cover</title>
<link rel="stylesheet" href="https://fonts.googleapis.com/css2?family=Poppins:wght@300;400;500;700;800&display=swap">
<style>
  :root {
    --backdrop: #f6e2cc;
    --navy: #13223d;
    --navy-deep: #0b1628;
    --orange: #d9843a;
    --yellow: #d8cc5c;
    --paper: #f1f1f1;
    --ink-light: #e6e9ef;
    --logo-navy: #0f1c33;
  }
  * { box-sizing: border-box; margin: 0; padding: 0; }
  html, body { width: 1200px; height: 800px; overflow: hidden; }
  body {
    background: var(--backdrop);
    font-family: "Poppins", sans-serif;
    display: flex;
    align-items: center;
    justify-content: center;
  }
  .spread {
    display: flex;
    width: 1018px;
    height: 720px;
    box-shadow: 0 10px 30px rgba(90, 60, 30, .18);
  }
  .page {
    position: relative;
    width: 509px;
    height: 720px;
    background: var(--navy);
    overflow: hidden;
  }
  .top-band {
    position: absolute; left: 0; top: 0;
    width: 100%; height: 30px;
    background: var(--orange);
  }
  .photo { position: absolute; left: 0; width: 100%; }

  /* back cover */
  .back .photo-oldcity {
    top: 30px; height: 400px;
    background: linear-gradient(180deg, #5b6d86 0%, #8a8f8e 35%, #a2906a 60%, #4d5566 85%, var(--navy) 100%);
  }
  .contact {
    position: absolute; left: 70px; top: 470px;
    color: var(--ink-light);
    font-size: 11px; line-height: 1.55; font-weight: 400;
  }
  .contact-row { display: flex; gap: 12px; margin-bottom: 14px; }
  .contact-icon {
    flex: none; width: 22px; height: 22px; border-radius: 50%;
    background: var(--orange);
    display: flex; align-items: center; justify-content: center;
  }
  .web { letter-spacing: 2px; margin-left: 34px; }

  .foot-stripes {
    position: absolute; bottom: 34px; left: 0;
    display: flex; height: 56px;
  }
  .foot-stripes span { width: 12px; height: 100%; }
  .foot-stripes .s-navy { background: #25385a; }
  .foot-stripes .s-yellow { background: var(--yellow); }
  .foot-stripes .s-orange { background: var(--orange); }
  .foot-band {
    position: absolute; left: 0; bottom: 0;
    width: 100%; height: 60px;
    background: var(--navy-deep);
    border-top: 1px solid #2f3f5c;
  }

  /* front cover */
  .front .brand-area {
    position: absolute; top: 30px; left: 0;
    width: 100%; height: 140px;
    background: var(--paper);
    display: flex; align-items: center; justify-content: center; gap: 12px;
  }
  .brand-mark {
    width: 34px; height: 34px; border-radius: 50%;
    background: var(--orange);
  }
  .brand-name {
    font-size: 44px; font-weight: 800; color: var(--logo-navy);
    letter-spacing: -1px;
  }
  .front .photo-coast {
    top: 170px; height: 330px;
    background: linear-gradient(180deg, #b7c9d9 0%, #3d86a8 28%, #d9cdb4 55%, #c9a27c 78%, #5f7a45 100%);
  }
  .headline {
    position: absolute; left: 44px; top: 540px;
    color: var(--yellow);
  }
  .headline .lead {
    font-size: 27px; font-weight: 800; letter-spacing: .3px; line-height: 1.1;
  }
  .headline .sub {
    font-size: 26px; font-weight: 300; line-height: 1.25;
  }
  .front-footer {
    position: absolute; left: 0; bottom: 0;
    width: 100%; height: 60px;
    background: var(--navy-deep);
    border-top: 1px solid #2f3f5c;
    color: var(--ink-light);
    font-size: 10.5px;
    display: flex; align-items: center; justify-content: flex-end;
    padding-right: 40px;
  }
</style>
</head>
<body>
  <main class="spread">
    <section class="page back">
      <div class="top-band"></div>
      <div class="photo photo-oldcity" role="img" aria-label="Photo of an old walled city plaza with a golden dome under a cloudy sky"></div>
      <div class="contact">
        <div class="contact-row">
          <div class="contact-icon">
            <svg width="12" height="12" viewBox="0 0 12 12"><path d="M6 1a3.5 3.5 0 0 0-3.5 3.5C2.5 7 6 11 6 11s3.5-4 3.5-6.5A3.5 3.5 0 0 0 6 1z" fill="none" stroke="#fff" stroke-width="1.1"/><circle cx="6" cy="4.5" r="1.2" fill="none" stroke="#fff" stroke-width="1"/></svg>
          </div>
          <p>1187 Larkspur Lane Edenvale, MN 55390<br>418 W 71st St Suite 3B New York, NY 10023<br>Phone: 1-800-555-0142</p>
        </div>
        <div class="contact-row">
          <div class="contact-icon">
            <svg width="12" height="12" viewBox="0 0 12 12"><rect x="1.5" y="2" width="9" height="6" rx=".8" fill="none" stroke="#fff" stroke-width="1.1"/><path d="M4 10h4M6 8v2" stroke="#fff" stroke-width="1.1"/></svg>
          </div>
          <p>HaTamar 12b, Kfar Ronen, Israel 4051200<br>Phone: 972-54-5550187</p>
        </div>
        <p class="web">Web : www.gowayfarlo.com</p>
      </div>
      <div class="foot-band"></div>
      <div class="foot-stripes"><span class="s-navy"></span><span class="s-yellow"></span><span class="s-orange"></span></div>
    </section>

    <section class="page front">
      <div class="top-band"></div>
      <div class="brand-area">
        <span class="brand-mark"></span>
        <span class="brand-name">Wayfarlo</span>
      </div>
      <div class="photo photo-coast" role="img" aria-label="Photo of a sunny city beach with sea, sand, bathers and a skyline along the shore"></div>
      <div class="headline">
        <p class="lead">WE AREN’T A TOUR PROVIDER</p>
        <p class="sub">We Are An Experience Maker</p>
      </div>
      <div class="front-footer">HaTamar 12b, Kfar Ronen, Israel 4051200 | 972-54-5550187</div>
      <div class="foot-stripes"><span class="s-navy"></span><span class="s-yellow"></span><span class="s-orange"></span></div>
    </section>
  </main>
</body>
</html>
```